Flyer für Unternehmensberatung für ambulante Pflegedienste
Zielgruppe
Wir sind eine Unternehmsberatung für ambulante Pflegedienste. Es wird ein Flyer und eine Anzeige in gleichem Design benötigt
Aufgabenstellung
Vorderseite
Headline / Titel
KORELO – Unternehmensberatung für ambulante Pflegedienste
Sub Headline / Slogan
Wirtschaftlichkeit stärken. Prozesse optimieren. Zukunft sichern.
Kurze Einführung / Elevator Pitch
Sie sind Pflegedienst Inhaber*in oder Führungskraft und stehen täglich vor wirtschaftlichen Herausforderungen?
Unser interdisziplinäres Experten Team von Korelo analysiert Ihre Tourenpläne, Leistungskalkulationen und Kennzahlen – und zeigt, wie Sie Ihre Pflege¬leistungen ökonomisch optimieren und gleichzeitig Ihre Pflegequalität sichern.
Leistungen im Überblick
Unsere Beratungsfelder im Überblick:
• Tourenplananalyse & Routenoptimierung
Wir untersuchen Fahr und Besuchsstrukturen, identifizieren Leerlauf, optimieren Einsatzzeiten und steigern die Effizienz.
• Kosten und Leistungsrechnung
Wir prüfen Ihre Kostenstruktur, Leistungserfassung und Vergütungsmodelle – um optimale Deckungsbeiträge zu erreichen.
• Kennzahlen Monitoring
Von Pflegestunden pro Klient bis Personalkostenquote – wir definieren die relevanten KPIs, vergleichen Soll Ist Werte und entwickeln praxisnahe Maßnahmen.
• Prozess und Organisationsberatung
Wir begleiten Sie bei der Digitalisierung, dem QM System, Personalmanagement und bei strategischen Entscheidungen (z. B. Expansion, Kooperationen).
Warum Korelo?
• Erfahren & praxisnah: Unser Team besteht aus ehemaligen Leitungskräften, Pflegefachkräften und Betriebswirt*innen mit Fokus auf ambulante Pflege.
• 100 % professionell geführt: Wir arbeiten strukturiert, belastbar und transparent – analog zu den hohen Anforderungen in Ihrem Alltag.
• Maßgeschneiderte Lösungen: Keine Standardberatung, sondern passgenau für Ihre Strukturen – sofort umsetzbar.
Jetzt Erstgespräch anfragen – kostenf..

```html
<!DOCTYPE html>
<html lang="de">
<head>
<meta charset="utf-8">
<title>KORELO – Unternehmensberatung für Ambulante Pflegedienste</title>
<link rel="stylesheet" href="https://fonts.googleapis.com/css2?family=Inter:wght@400;500;700&display=swap">
<style>
  :root {
    --sky: #deeef6;
    --ink: #0f1d21;
    --halo: #c9dcd8;
    --photo-a: #8fb0cf;
    --photo-b: #e6ddd4;
    --card-blue: #a9c5d6;
    --card-mint: #cfe6d3;
    --card-rose: #e8c5c4;
    --card-sage: #93bf95;
    --icon-fill: #7fae82;
    --white: #ffffff;
  }
  * { box-sizing: border-box; margin: 0; padding: 0; }
  html, body { width: 1200px; height: 900px; overflow: hidden; }
  body { font-family: "Inter", Arial, sans-serif; color: var(--ink); background: var(--sky); }
  .flyer { position: relative; width: 1200px; height: 900px; overflow: hidden; background: var(--sky); }

  .hero-halo { position: absolute; left: 825px; top: 70px; width: 560px; height: 560px; border-radius: 50%; background: var(--halo); }
  .hero-photo { position: absolute; left: 850px; top: 100px; width: 350px; height: 485px;
    background: linear-gradient(180deg, var(--photo-b) 0%, #b8cfe0 45%, var(--photo-a) 100%);
    border-top-left-radius: 180px; }

  .headline { position: absolute; left: 92px; top: 48px; font-size: 45px; font-weight: 700; line-height: 1.18; letter-spacing: -0.3px; }
  .slogan { position: absolute; left: 92px; top: 347px; font-size: 22px; line-height: 1.5; font-weight: 400; }
  .cta { position: absolute; left: 92px; top: 507px; width: 310px; height: 75px; border-radius: 38px; background: var(--ink); color: var(--white);
    display: flex; align-items: center; justify-content: center; text-align: center; font-size: 16.5px; line-height: 1.4; font-weight: 500; text-transform: uppercase; }

  .portrait { position: absolute; border-radius: 50%; border: 4px solid var(--white); box-shadow: 0 4px 14px rgba(0,0,0,.15); }
  .portrait-one { left: 742px; top: 213px; width: 160px; height: 160px; background: linear-gradient(160deg, #eceae6, #b9b3ab); }
  .portrait-two { left: 772px; top: 452px; width: 150px; height: 150px; background: linear-gradient(160deg, #dfe3e6, #7d8a97); }
  .portrait-three { left: 965px; top: 420px; width: 168px; height: 168px; background: linear-gradient(160deg, #eef0f0, #c9b79b); }

  .bubble { position: absolute; left: 1035px; top: 18px; width: 146px; height: 146px; border-radius: 50%; background: var(--ink); color: var(--white);
    display: flex; align-items: center; justify-content: center; text-align: center; font-size: 19px; font-weight: 500; line-height: 1.3; }
  .bubble-tail { position: absolute; left: 1030px; top: 125px; }

  .services { position: absolute; left: 0; top: 585px; width: 1200px; height: 315px; display: grid; grid-template-columns: repeat(4, 1fr); }
  .service { padding: 36px 24px 0 50px; }
  .service-blue { background: var(--card-blue); }
  .service-mint { background: var(--card-mint); }
  .service-rose { background: var(--card-rose); }
  .service-sage { background: var(--card-sage); }
  .service-icon { display: block; margin: 0 auto 0 68px; width: 50px; height: 50px; }
  .service-title { margin-top: 38px; font-size: 24px; font-weight: 500; line-height: 1.2; }
  .service-text { margin-top: 12px; font-size: 16.5px; line-height: 1.42; }
  .service-sage .service-title { margin-top: 38px; }
</style>
</head>
<body>
<main class="flyer">
  <div class="hero-halo"></div>
  <div class="hero-photo" role="img" aria-label="Lächelnde Pflegefachkraft in blauer Dienstkleidung mit Stethoskop"></div>

  <h1 class="headline">KORELO –<br>Unternehmens-<br>Unternehmensberatung<br>für Ambulante<br>Pflegedienste</h1>
  <p class="slogan">Strengthen profitability. Optimize<br>processes. Secure the future.</p>
  <div class="cta">Book a free online<br>consultation today</div>

  <div class="portrait portrait-one" role="img" aria-label="Porträt einer älteren Klientin, winkend"></div>
  <div class="portrait portrait-two" role="img" aria-label="Porträt eines Beraters im weißen Kittel"></div>
  <div class="portrait portrait-three" role="img" aria-label="Porträt einer Ärztin mit Brille"></div>

  <svg class="bubble-tail" width="40" height="40" viewBox="0 0 40 40" aria-hidden="true"><path d="M18 0 L40 8 L0 34 Z" fill="#0f1d21"/></svg>
  <div class="bubble">BOOK NOW<br>TODAY</div>

  <section class="services">
    <article class="service service-blue">
      <svg class="service-icon" viewBox="0 0 50 50" aria-hidden="true">
        <path d="M4 12 H18 M4 20 H14 M36 6 V22 M28 14 H44" stroke="#0f1d21" stroke-width="2.2" fill="none"/>
        <rect x="6" y="30" width="12" height="14" rx="1.5" fill="#7fae82" stroke="#0f1d21" stroke-width="2"/>
        <rect x="22" y="24" width="12" height="20" rx="1.5" fill="#7fae82" stroke="#0f1d21" stroke-width="2"/>
      </svg>
      <h2 class="service-title">Route Planning</h2>
      <p class="service-text">Leerlauf erkennen, Einsatzzeiten optimieren und Fahrstrukturen effizient planen für Ihr Team.</p>
    </article>
    <article class="service service-mint">
      <svg class="service-icon" viewBox="0 0 50 50" aria-hidden="true">
        <path d="M6 8 H26 M6 16 H22 M6 24 H18 M10 4 V28" stroke="#0f1d21" stroke-width="2.2" fill="none"/>
        <circle cx="32" cy="32" r="13" fill="none" stroke="#0f1d21" stroke-width="2.2"/>
        <circle cx="32" cy="32" r="7" fill="#7fae82" stroke="#0f1d21" stroke-width="2"/>
      </svg>
      <h2 class="service-title">Cost Control</h2>
      <p class="service-text">Kostenstruktur prüfen, Leistungen erfassen und Vergütung sichern für starke Deckungsbeiträge.</p>
    </article>
    <article class="service service-rose">
      <svg class="service-icon" viewBox="0 0 50 50" aria-hidden="true">
        <path d="M12 20 L4 12 A5 5 0 0 1 12 5 A5 5 0 0 1 20 12 Z" fill="none" stroke="#0f1d21" stroke-width="2.2"/>
        <circle cx="10" cy="40" r="4" fill="none" stroke="#0f1d21" stroke-width="2.2"/>
        <rect x="20" y="30" width="6" height="14" rx="3" fill="none" stroke="#0f1d21" stroke-width="2.2"/>
        <rect x="30" y="20" width="6" height="24" rx="3" fill="none" stroke="#0f1d21" stroke-width="2.2"/>
        <rect x="40" y="26" width="6" height="18" rx="3" fill="none" stroke="#0f1d21" stroke-width="2.2"/>
      </svg>
      <h2 class="service-title">KPI Evaluation</h2>
      <p class="service-text">Soll-Ist-Werte vergleichen, relevante KPIs definieren und praxisnahe Maßnahmen ableiten.</p>
    </article>
    <article class="service service-sage">
      <svg class="service-icon" viewBox="0 0 50 50" aria-hidden="true">
        <rect x="0" y="0" width="50" height="50" rx="12" fill="#ffffff"/>
        <path d="M25 34 L16 25 A5 5 0 0 1 25 18 A5 5 0 0 1 34 25 Z" fill="#7fae82"/>
      </svg>
      <h2 class="service-title">Digital Process<br>Support</h2>
      <p class="service-text">Digitalisierung, QM-System und Personalmanagement begleiten – strategisch und sofort umsetzbar.</p>
    </article>
  </section>
</main>
</body>
</html>
```